Powerpoint template for trainer and coach in the field of personality development

Powerpoint template for coach and coach in the field of personality development I would like to have a basic design for Powerpoint 2007. It should work: clear, friendly, aesthetic, modern, simple, simple, beautiful, unique, at the same time warm and emotional ("masculine" in the settings seems to lead to rather cool designs). It's about aspects of personality development, psychology, human behavior, which of course has a lot to do with feelings. The lecture, which is based on the presentation, will also be more emotionally colored with objective background than the other. This personal level must be able to transport the design without being too flowery or playful or childish. (I know, maybe it's difficult :-) Charts and statistics are rather rare I would like a basic design for Powerpoint 2007. It should work: clear, friendly, friendly, aesthetic, modern, simple, simple, beautiful, clear, warm and emotional at the same time ("masculine" in the settings seems to lead to rather cool designs). It is about aspects of personality development, psychology and human behavior, which has a lot to do with feelings. So the presentation, which is based on the presentation, wants to be more emotionally colored with a factual background than the other way around. This personal level must be able to transport the design without appearing too flowery or playful or childlike. (I know, it may be difficult: -) Charts and statistics are rather rare Please refer to my previous CI: Logo Website: lukas-femberg. de Workshop-Flyer White as a background colored (red) bar top logo below small would be possible But I can imagine color as a basic background Make suggestions to your taste please and can not be restricted by my ideas The information on the color comes from mine previous agency, I hope you agree. In principle, elements can also be used in the following order: Word document template for handout - seminar materials or offer. Please contact me if you have any questions Best regards I would like a basic design for Powerpoint 2007. It should work: clear, friendly, aesthetic, modern, simple, simple, beautiful, clear Please refer to my previous CI: logo Website: lukas- Fembërg. de workshop flyer White background (red) bar at the top of the page. Can you make a color change? The information on the color comes from my previous agency, I hope they are correct. In principle, elements can also be used in the following order: Word document template for handout - seminar materials or offer. With kind regards Color: Red CMYK: 15% Cyan 100% Magenta 100% Yellow 0% Black RGB Dec: 204, 7, 30 RGB%: 80 - 2.7 - 11.8

Target Market(s)

Personnel Developers - Managers -. Employees of companies Also from social enterprises and NGO Personnel developers - executives -. corporate employees So from social enterprises and NGOs

Font styles to use
Sans Serif

Colors
ec1f27

Requirements
Must have
• Title page incl. Logo content page text only: headline plus list No long texts. Only incrustations of max. 7 Punkte = Zeilen Content page Foto, beside Text (Aufzählung) Content page: Foto groß, on which several words as text Title page incl. Logo Content page only text: heading plus enumeration No long texts. Only enumerations of max. 7 points = lines Content page photo, next to it text (list) Contents page: photo large, on it several words as text
Nice to have
• Final page incl. QR code Final page including QR code
Should not have
• playfulness, very technical, cold, empirically oriented playful, very technical, cold, empirically oriented

```html
<!DOCTYPE html>
<html lang="en">
<head>
<meta charset="utf-8">
<title>Coaching Presentation Template – Slide Overview</title>
<link href="https://fonts.googleapis.com/css2?family=Arimo:wght@400;700&display=swap" rel="stylesheet">
<style>
:root{
  --red:#d42030;
  --pink:#e5177f;
  --dark:#231f20;
  --blue:#1ba3dc;
  --navy:#2e3690;
  --grey:#8a8a8a;
  --light:#dcdcdc;
  --canvas:#ececec;
}
html,body{margin:0;padding:0;overflow:hidden;}
body{width:1200px;height:1151px;background:var(--canvas);position:relative;font-family:Arimo,Arial,sans-serif;}
.slide{position:absolute;width:393px;height:220px;background:#fff;box-shadow:0 1px 3px rgba(0,0,0,.18);}
.slide text{font-family:Arimo,Arial,sans-serif;}
.ttl{font-size:15px;fill:var(--dark);}
.logo{font-size:10px;font-weight:700;fill:var(--red);}
.copy{font-size:5px;fill:#fff;}
.pg{font-size:5px;fill:#fff;}
.lorem{font-size:5.2px;fill:#9a9a9a;}
.lorem-w{font-size:6.6px;fill:#fff;}
.small{font-size:5px;fill:#555;}
.red{fill:var(--red);} .pink{fill:var(--pink);} .dark{fill:var(--dark);} .blue{fill:var(--blue);} .navy{fill:var(--navy);} .white{fill:#fff;}
.lbl{font-size:8.5px;}
</style>
</head>
<body>

<!-- Row 1 -->
<svg class="slide sales-comparison" style="left:3px;top:5px" viewBox="0 0 478 268">
  <text class="ttl" x="20" y="33">SALES COMPARISON</text>
  <rect class="red" x="20" y="40" width="26" height="2"/>
  <text class="logo" x="468" y="27" text-anchor="end">LUKAS FEMBERG</text>
  <text class="red" x="100" y="85" font-size="7.5" text-anchor="middle">2017 Sales</text>
  <g class="red">
    <rect x="35" y="110" width="14" height="66"/><rect x="73" y="133" width="14" height="43"/>
    <rect x="111" y="117" width="14" height="59"/><rect x="148" y="103" width="14" height="73"/>
  </g>
  <g class="small" font-size="4" text-anchor="middle">
    <text x="42" y="106" fill="#d42030">4.3</text><text x="80" y="130">2.5</text><text x="118" y="114">3.5</text><text x="155" y="100">4.5</text>
    <text x="42" y="182">2011</text><text x="80" y="182">2012</text><text x="118" y="182">2013</text><text x="155" y="182">2014</text>
  </g>
  <line x1="30" y1="176" x2="168" y2="176" stroke="#ccc" stroke-width=".6"/>
  <text class="red" x="34" y="220" font-size="24">45%</text>
  <text class="red" x="93" y="200" font-size="6.5">Lorem ipsum dolor</text>
  <text class="lorem" x="93" y="209">Lorem ipsum dolor sit amet</text>
  <text class="lorem" x="93" y="216">consectetur</text>
  <line x1="236" y1="78" x2="236" y2="232" stroke="#aaa" stroke-width="1" stroke-dasharray="2 2"/>
  <circle cx="229" cy="142" r="14" fill="#e5177f"/><circle cx="244" cy="142" r="14" fill="#e5177f" opacity=".75"/>
  <circle cx="236" cy="142" r="8" fill="#d42030"/>
  <text class="white" x="236" y="145" font-size="8" text-anchor="middle">VS</text>
  <text class="dark" x="378" y="85" font-size="7.5" text-anchor="middle">2018 Sales</text>
  <g class="dark">
    <rect x="310" y="112" width="14" height="64"/><rect x="347" y="138" width="14" height="38"/>
    <rect x="384" y="122" width="14" height="54"/><rect x="421" y="108" width="14" height="68"/>
  </g>
  <g class="small" font-size="4" text-anchor="middle">
    <text x="317" y="108">4.3</text><text x="354" y="134">2.5</text><text x="391" y="118">3.5</text><text x="428" y="104">4.5</text>
    <text x="317" y="182">2011</text><text x="354" y="182">2012</text><text x="391" y="182">2013</text><text x="428" y="182">2014</text>
  </g>
  <line x1="304" y1="176" x2="442" y2="176" stroke="#ccc" stroke-width=".6"/>
  <text class="dark" x="308" y="220" font-size="24">68%</text>
  <text class="dark" x="366" y="200" font-size="6.5">Lorem ipsum dolor</text>
  <text class="lorem" x="366" y="209">Lorem ipsum dolor sit amet</text>
  <text class="lorem" x="366" y="216">consectetur</text>
  <rect class="red" x="0" y="254" width="478" height="14"/>
  <text class="copy" x="20" y="263">© Copyright 2017 Lukas Femberg. All rights reserved.</text>
  <rect class="dark" x="430" y="254" width="28" height="14"/><text class="pg" x="444" y="263" text-anchor="middle">37</text>
</svg>

<svg class="slide title-slide" style="left:403px;top:5px" viewBox="0 0 478 268">
  <defs><linearGradient id="titleBg" x1="0" y1="0" x2="0" y2="1"><stop offset="0" stop-color="#d9d9d9"/><stop offset="1" stop-color="#bdbdbd"/></linearGradient></defs>
  <rect width="478" height="268" fill="url(#titleBg)" role="img" aria-label="Soft grey background photograph"/>
  <text x="239" y="54" font-size="15" fill="#fff" text-anchor="middle">YOUR TITLE GOES HERE</text>
  <rect class="red" x="226" y="61" width="26" height="2"/>
  <rect x="0" y="124" width="160" height="121" fill="#d65560"/>
  <rect x="160" y="124" width="159" height="121" fill="#555"/>
  <rect x="319" y="124" width="159" height="121" fill="#e4519a"/>
  <g class="lorem-w">
    <text x="18" y="146">Lorem ipsum dolor sit amet,</text><text x="18" y="156">consectetur adipiscing elit, sed do</text><text x="18" y="165">eiusmod tempor incididunt ut</text><text x="18" y="175">labore et dolore magna aliqua. Ut</text><text x="18" y="184">enimad minim veniam, quis</text><text x="18" y="194">nostrud exercitation ullamco</text><text x="18" y="203">laboris nisi ut aliquip ex ea</text><text x="18" y="213">commodo consequat.</text>
    <text x="178" y="146">Lorem ipsum dolor sit amet,</text><text x="178" y="156">consectetur adipiscing elit, sed do</text><text x="178" y="165">eiusmod tempor incididunt ut</text><text x="178" y="175">labore et dolore magna aliqua. Ut</text><text x="178" y="184">enimad minim veniam, quis</text><text x="178" y="194">nostrud exercitation ullamco</text><text x="178" y="203">laboris nisi ut aliquip ex ea</text><text x="178" y="213">commodo consequat.</text>
    <text x="338" y="146">Lorem ipsum dolor sit amet,</text><text x="338" y="156">consectetur adipiscing elit, sed do</text><text x="338" y="165">eiusmod tempor incididunt ut</text><text x="338" y="175">labore et dolore magna aliqua. Ut</text><text x="338" y="184">enimad minim veniam, quis</text><text x="338" y="194">nostrud exercitation ullamco</text><text x="338" y="203">laboris nisi ut aliquip ex ea</text><text x="338" y="213">commodo consequat.</text>
  </g>
</svg>

<svg class="slide photo-text" style="left:802px;top:5px" viewBox="0 0 478 268">
  <defs><linearGradient id="waterPhoto" x1="0" y1="0" x2="1" y2="1"><stop offset="0" stop-color="#e4e8e8"/><stop offset=".6" stop-color="#b7bfbf"/><stop offset="1" stop-color="#6f7676"/></linearGradient></defs>
  <text class="ttl" x="20" y="33">YOUR TITLE</text><rect class="red" x="20" y="40" width="26" height="2"/>
  <rect x="238" y="0" width="240" height="135" fill="url(#waterPhoto)" role="img" aria-label="Photo of a kayaker paddling through white water"/>
  <path d="M35 69 l7 7 -7 7 -7 -7z" fill="none" stroke="#d42030" stroke-width="2"/>
  <text class="red lbl" x="48" y="80">Bullet Point</text>
  <text class="lorem" x="48" y="89">Lorem ipsum dolor sit amet, consectetur adipiscing</text>
  <text class="lorem" x="48" y="96">elit, sed do eiusmod tempor incididunt ut labore et</text>
  <text class="lorem" x="48" y="103">dolore magna aliqua.</text>
  <rect class="red" x="0" y="135" width="238" height="133"/>
  <g class="lorem-w"><text x="14" y="171">Lorem ipsum dolor sit amet, consectetur adipiscing elit, sed</text><text x="14" y="180">do eiusmod tempor incididunt ut labore et dolore magna</text><text x="14" y="189">aliqua. Ut enimad minim veniam, quis nostrud exercitation</text><text x="14" y="198">ullamco laboris nisi ut aliquip ex ea commodo consequat.</text><text x="14" y="219">Duis aute irure dolor in reprehenderit in voluptate velit esse</text><text x="14" y="228">cillum dolore eu fugiat nulla pariatur excepteur.</text></g>
  <g class="pink"><rect x="270" y="184" width="2" height="8"/><rect x="274" y="181" width="2" height="11"/><rect x="278" y="186" width="2" height="6"/><rect x="282" y="183" width="2" height="9"/></g>
  <text class="pink lbl" x="298" y="190">Bullet Point</text>
  <text class="lorem" x="298" y="199">Lorem ipsum dolor sit amet, consectetur adipiscing</text>
  <text class="lorem" x="298" y="206">elit, sed do eiusmod tempor incididunt ut labore et</text>
  <text class="lorem" x="298" y="213">dolore magna aliqua.</text>
</svg>

<!-- Row 2 -->
<svg class="slide photo-text" style="left:3px;top:234px" viewBox="0 0 478 268">
  <defs><linearGradient id="bridgePhoto" x1="0" y1="0" x2="1" y2="1"><stop offset="0" stop-color="#6b5a44"/><stop offset=".5" stop-color="#a89377"/><stop offset="1" stop-color="#4a3e30"/></linearGradient></defs>
  <text class="ttl" x="20" y="33">YOUR TITLE</text><rect class="red" x="20" y="40" width="26" height="2"/>
  <rect x="238" y="0" width="240" height="135" fill="url(#bridgePhoto)" role="img" aria-label="Photo of a wooden rope bridge in a forest"/>
  <rect class="pink" x="238" y="135" width="240" height="133"/>
  <g class="lorem-w"><text x="253" y="176">Lorem ipsum dolor sit amet, consectetur adipiscing elit, sed</text><text x="253" y="185">do eiusmod tempor incididunt ut labore et dolore magna</text><text x="253" y="194">aliqua. Ut enimad minim veniam, quis nostrud exercitation</text><text x="253" y="203">ullamco laboris nisi ut aliquip ex ea commodo consequat.</text><text x="253" y="223">Duis aute irure dolor in reprehenderit in voluptate velit esse</text><text x="253" y="232">cillum dolore eu fugiat nulla pariatur excepteur.</text></g>
  <path d="M34 69 l7 7 -7 7 -7 -7z" fill="none" stroke="#d42030" stroke-width="2"/>
  <text class="red lbl" x="48" y="80">Bullet Point</text>
  <text class="lorem" x="48" y="89">Lorem ipsum dolor sit amet, consectetur adipiscing</text><text class="lorem" x="48" y="96">elit, sed do eiusmod tempor incididunt ut labore et</text><text class="lorem" x="48" y="103">dolore magna aliqua.</text>
  <g fill="#666"><rect x="28" y="136" width="2" height="9"/><rect x="32" y="133" width="2" height="12"/><rect x="36" y="138" width="2" height="7"/><rect x="40" y="135" width="2" height="10"/></g>
  <text class="dark lbl" x="48" y="145">Chart</text>
  <text class="lorem" x="48" y="154">Lorem ipsum dolor sit amer, consectetur adipiscing</text><text class="lorem" x="48" y="161">elit, sed do eiusmod tempor incididunt ut labore et</text><text class="lorem" x="48" y="168">dolore magna aliqua.</text>
  <g stroke="#d42030" stroke-width="1" fill="none"><circle cx="28" cy="202" r="2.5"/><circle cx="37" cy="197" r="2.5"/><circle cx="37" cy="208" r="2.5"/><path d="M30 201 L35 198 M30 203 L35 207"/></g>
  <text class="red lbl" x="48" y="207">Share</text>
  <text class="lorem" x="48" y="216">Lorem ipsum dolor sit amet, consectetur adipiscing</text><text class="lorem" x="48" y="223">elit, sed do eiusmod tempor incididunt ut labore et</text><text class="lorem" x="48" y="230">dolore magna aliqua.</text>
</svg>

<svg class="slide project-timeline" style="left:403px;top:234px" viewBox="0 0 478 268">
  <text class="ttl" x="20" y="33">PROJECT TIMELINE</text><rect class="red" x="20" y="40" width="26" height="2"/>
  <text class="logo" x="468" y="27" text-anchor="end">LUKAS FEMBERG</text>
  <g class="small" font-size="5.5" text-anchor="middle">
    <text x="85" y="75">Project step</text><text x="146" y="75">Jan</text><text x="172" y="75">Feb</text><text x="198" y="75">Mar</text><text x="224" y="75">Apr</text><text x="250" y="75">May</text><text x="276" y="75">June</text><text x="302" y="75">July</text><text x="328" y="75">Aug</text><text x="354" y="75">Sep</text><text x="380" y="75">Oct</text><text x="406" y="75">Nov</text><text x="432" y="75">Dec</text>
  </g>
  <g stroke="#cfcfcf" stroke-width=".5" fill="none">
    <rect x="38" y="79" width="408" height="126"/>
    <path d="M38 93H446M38 107H446M38 121H446M38 135H446M38 149H446M38 163H446M38 177H446M38 191H446"/>
    <path d="M133 79V205M159 79V205M185 79V205M211 79V205M237 79V205M263 79V205M289 79V205M315 79V205M341 79V205M367 79V205M393 79V205M419 79V205"/>
  </g>
  <g class="small" font-size="4.5" text-anchor="middle">
    <text x="85" y="88">Process 01</text><text x="85" y="102">Process 02</text><text x="85" y="116">Process 03</text><text x="85" y="130">Process 04</text><text x="85" y="144">Process 05</text><text x="85" y="158">Process 06</text><text x="85" y="172">Process 07</text><text x="85" y="186">Process 08</text><text x="85" y="200">Process 09</text>
  </g>
  <g stroke-width="6" stroke-linecap="round">
    <path d="M147 86H188" stroke="#d42030"/><path d="M378 86H432" stroke="#231f20"/>
    <path d="M180 100H198" stroke="#d42030"/><path d="M256 100H290" stroke="#d42030"/>
    <path d="M201 114H333" stroke="#231f20"/>
    <path d="M224 128H273" stroke="#e5177f"/><path d="M337 128H368" stroke="#231f20"/>
    <path d="M298 142H433" stroke="#e5177f"/>
    <path d="M220 156H260" stroke="#1ba3dc"/>
    <path d="M254 170H304" stroke="#1ba3dc"/>
    <path d="M308 184H344" stroke="#2e3690"/>
    <path d="M363 198H415" stroke="#2e3690"/>
  </g>
  <g font-size="5" fill="#777">
    <circle cx="92" cy="219" r="2" class="red"/><text x="97" y="221">Description</text>
    <circle cx="149" cy="219" r="2" class="dark"/><text x="154" y="221">Description</text>
    <circle cx="208" cy="219" r="2" class="pink"/><text x="213" y="221">Description</text>
    <circle cx="269" cy="219" r="2" class="blue"/><text x="274" y="221">Description</text>
    <circle cx="331" cy="219" r="2" class="navy"/><text x="336" y="221">Description</text>
  </g>
  <rect class="red" x="0" y="254" width="478" height="14"/>
  <text class="copy" x="20" y="263">© Copyright 2017 Lukas Femberg. All rights reserved.</text>
  <rect class="dark" x="430" y="254" width="28" height="14"/><text class="pg" x="444" y="263" text-anchor="middle">41</text>
</svg>

<svg class="slide who-we-are" style="left:802px;top:234px" viewBox="0 0 478 268">
  <text class="ttl" x="20" y="33">WHO WE ARE?</text><rect class="red" x="20" y="40" width="26" height="2"/>
  <text class="logo" x="468" y="27" text-anchor="end">LUKAS FEMBERG</text>
  <g font-size="12">
    <text class="red" x="36" y="76">A Title About</text><text class="red" x="36" y="92">Contents</text>
    <text class="dark" x="36" y="138">A Title About</text><text class="dark" x="36" y="154">Contents</text>
    <text class="red" x="36" y="200">A Title About</text><text class="red" x="36" y="216">Contents</text>
  </g>
  <text class="red" x="36" y="102" font-size="5">Lorem ipsum dolor sit</text>
  <text class="dark" x="36" y="164" font-size="5">Lorem ipsum dolor sit</text>
  <text class="red" x="36" y="226" font-size="5">Lorem ipsum dolor sit</text>
  <g font-size="5" fill="#999"><text x="147" y="68">2016</text><text x="147" y="130">2017</text><text x="147" y="192">2018</text></g>
  <line x1="147" y1="72" x2="444" y2="72" stroke="#d42030" stroke-width="1"/>
  <line x1="147" y1="134" x2="444" y2="134" stroke="#231f20" stroke-width="1"/>
  <line x1="147" y1="196" x2="444" y2="196" stroke="#e5177f" stroke-width="1"/>
  <g class="lorem">
    <text x="147" y="82">Lorem ipsum dolor sit amet, consectetur adipiscing elit, sed do eiusmod tempor</text><text x="147" y="89">incididunt ut labore et dolore aliqua. Lorem ipsum dolor sit amet, consectetur adipiscing</text><text x="147" y="96">elit, sed do eiusmod tempor incididunt ut labore</text>
    <text x="147" y="144">Lorem ipsum dolor sit amet, consectetur adipiscing elit, sed do eiusmod tempor</text><text x="147" y="151">incididunt ut labore et dolore aliqua. Lorem ipsum dolor sit amet, consectetur adipiscing</text><text x="147" y="158">elit, sed do eiusmod tempor incididunt ut labore</text>
    <text x="147" y="206">Lorem ipsum dolor sit amet, consectetur adipiscing elit, sed do eiusmod tempor</text><text x="147" y="213">incididunt ut labore et dolore aliqua. Lorem ipsum dolor sit amet, consectetur adipiscing</text><text x="147" y="220">elit, sed do eiusmod tempor incididunt ut labore</text>
  </g>
  <rect class="red" x="0" y="254" width="478" height="14"/>
  <text class="copy" x="20" y="263">© Copyright 2017 Lukas Femberg. All rights reserved.</text>
  <rect class="dark" x="430" y="254" width="28" height="14"/><text class="pg" x="444" y="263" text-anchor="middle">42</text>
</svg>

<!-- Row 3 -->
<svg class="slide bullet-chart" style="left:3px;top:464px" viewBox="0 0 478 268">
  <text class="ttl" x="20" y="33">BULLET &amp; CHART AREA</text><rect class="red" x="20" y="40" width="26" height="2"/>
  <text class="logo" x="468" y="27" text-anchor="end">LUKAS FEMBERG</text>
  <path d="M135 146 L135 88 A58 58 0 1 1 120.6 202.2Z" fill="#d42030"/>
  <path d="M135 146 L120.6 202.2 A58 58 0 0 1 78.8 131.6Z" fill="#231f20"/>
  <path d="M135 146 L78.8 131.6 A58 58 0 0 1 107.1 95.2Z" fill="#e5177f"/>
  <path d="M135 146 L107.1 95.2 A58 58 0 0 1 135 88Z" fill="#1ba3dc"/>
  <g fill="none" stroke="#fff" stroke-width="1"><path d="M135 146 L135 88M135 146 L120.6 202.2M135 146 L78.8 131.6M135 146 L107.1 95.2"/></g>
  <text class="blue" x="91" y="84" font-size="14">10%</text>
  <text class="pink" x="46" y="121" font-size="14">15%</text>
  <text class="dark" x="46" y="188" font-size="14">25%</text>
  <text class="red" x="197" y="154" font-size="14">60%</text>
  <g font-size="4.5" fill="#777"><rect class="red" x="80" y="215" width="3" height="3"/><text x="85" y="218">1st Qtr</text><rect class="dark" x="108" y="215" width="3" height="3"/><text x="113" y="218">2nd Qtr</text><rect class="pink" x="138" y="215" width="3" height="3"/><text x="143" y="218">3rd Qtr</text><rect class="blue" x="166" y="215" width="3" height="3"/><text x="171" y="218">4th Qtr</text></g>
  <g>
    <circle cx="270" cy="86" r="10" class="red"/><circle cx="269" cy="85" r="3" fill="none" stroke="#fff" stroke-width="1.2"/><path d="M271 87 l3 3" stroke="#fff" stroke-width="1.2"/>
    <text class="red lbl" x="290" y="84">Category One</text><text class="lorem" x="290" y="92">Lorem ipsum dolor sit amet, consectetur</text><text class="lorem" x="290" y="98">adipiscing elit, sed do eiusmod</text>
    <circle cx="270" cy="126" r="10" class="dark"/><path d="M266 130 l8 -8" stroke="#fff" stroke-width="2"/>
    <text class="dark lbl" x="290" y="124">Category Two</text><text class="lorem" x="290" y="132">Lorem ipsum dolor sit amet, consectetur</text><text class="lorem" x="290" y="138">adipiscing elit, sed do eiusmod</text>
    <circle cx="270" cy="164" r="10" class="pink"/><path d="M266 168 l4 -8 4 4z" fill="#fff"/>
    <text class="pink lbl" x="290" y="162">Category Three</text><text class="lorem" x="290" y="170">Lorem ipsum dolor sit amet, consectetur</text><text class="lorem" x="290" y="176">adipiscing elit, sed do eiusmod</text>
    <circle cx="270" cy="203" r="10" class="blue"/><circle cx="270" cy="203" r="4" fill="none" stroke="#fff" stroke-width="2" stroke-dasharray="2 1"/>
    <text class="blue lbl" x="290" y="201">Category Four</text><text class="lorem" x="290" y="209">Lorem ipsum dolor sit amet, consectetur</text><text class="lorem" x="290" y="215">adipiscing elit, sed do eiusmod</text>
  </g>
  <rect class="red" x="0" y="254" width="478" height="14"/>
  <text class="copy" x="20" y="263">© Copyright 2017 Lukas Femberg. All rights reserved.</text>
  <rect class="dark" x="430" y="254" width="28" height="14"/><text class="pg" x="444" y="263" text-anchor="middle">43</text>
</svg>

<svg class="slide pie-text" style="left:403px;top:464px" viewBox="0 0 478 268">
  <text class="ttl" x="20" y="33">PIE CHART AND TEXT</text><rect class="red" x="20" y="40" width="26" height="2"/>
  <text class="logo" x="468" y="27" text-anchor="end">LUKAS FEMBERG</text>
  <g stroke="#fff" stroke-width="3">
    <path d="M127 138 L127 63 A75 75 0 0 1 171.1 198.7Z" fill="#d42030"/>
    <path d="M123 141 L167.1 201.7 A75 75 0 0 1 51.7 164.2Z" fill="#231f20"/>
    <path d="M121 138 L49.7 161.2 A75 75 0 0 1 76.9 78.3Z" fill="#e5177f"/>
    <path d="M123 136 L78.9 75.3 A75 75 0 0 1 123 61Z" fill="#1ba3dc"/>
  </g>
  <g fill="#fff" font-size="13"><text x="153" y="134">40%</text><text x="95" y="190">30%</text><text x="60" y="132">20%</text><text x="90" y="89">10%</text></g>
  <g font-size="4.5" fill="#777"><rect class="red" x="70" y="224" width="3" height="3"/><text x="75" y="227">1st Qtr</text><rect class="dark" x="98" y="224" width="3" height="3"/><text x="103" y="227">2nd Qtr</text><rect class="pink" x="128" y="224" width="3" height="3"/><text x="133" y="227">3rd Qtr</text><rect class="blue" x="156" y="224" width="3" height="3"/><text x="161" y="227">4th Qtr</text></g>
  <line x1="221" y1="65" x2="221" y2="215" stroke="#ddd" stroke-width="1"/>
  <g fill="#fff" stroke-width="1.2" font-size="11" text-anchor="middle">
    <circle cx="246" cy="78" r="11" stroke="#d42030"/><circle cx="246" cy="120" r="11" stroke="#231f20"/><circle cx="246" cy="161" r="11" stroke="#e5177f"/><circle cx="246" cy="202" r="11" stroke="#1ba3dc"/>
  </g>
  <g font-size="11" text-anchor="middle"><text class="red" x="246" y="82">1</text><text class="dark" x="246" y="124">2</text><text class="pink" x="246" y="165">3</text><text class="blue" x="246" y="206">4</text></g>
  <g font-size="5.5" fill="#555">
    <text x="267" y="73">Lorem ipsum dolor sit amet, consectetur adipiscing elit, sed do</text><text x="267" y="80">eiusmod tempor incididunt ut labore et dolore aliqua. Lorem</text><text x="267" y="87">ipsum dolor sit consectetur adipiscing elit</text>
    <text x="267" y="115">Lorem ipsum dolor sit amet, consectetur adipiscing elit, sed do</text><text x="267" y="122">eiusmod tempor incididunt ut labore et dolore aliqua. Lorem</text><text x="267" y="129">ipsum dolor sit consectetur adipiscing elit</text>
    <text x="267" y="156">Lorem ipsum dolor sit amet, consectetur adipiscing elit, sed do</text><text x="267" y="163">eiusmod tempor incididunt ut labore et dolore aliqua. Lorem</text><text x="267" y="170">ipsum dolor sit consectetur adipiscing elit</text>
    <text x="267" y="197">Lorem ipsum dolor sit amet, consectetur adipiscing elit, sed do</text><text x="267" y="204">eiusmod tempor incididunt ut labore et dolore aliqua. Lorem</text><text x="267" y="211">ipsum dolor sit consectetur adipiscing elit</text>
  </g>
  <rect class="red" x="0" y="254" width="478" height="14"/>
  <text class="copy" x="20" y="263">© Copyright 2017 Lukas Femberg. All rights reserved.</text>
  <rect class="dark" x="430" y="254" width="28" height="14"/><text class="pg" x="444" y="263" text-anchor="middle">44</text>
</svg>

<svg class="slide bullet-chart" style="left:802px;top:464px" viewBox="0 0 478 268">
  <text class="ttl" x="20" y="33">BULLET &amp; CHART AREA</text><rect class="red" x="20" y="40" width="26" height="2"/>
  <text class="logo" x="468" y="27" text-anchor="end">LUKAS FEMBERG</text>
  <line x1="70" y1="75" x2="70" y2="210" stroke="#ccc" stroke-width=".6"/>
  <g font-size="4.5" fill="#777" text-anchor="end"><text x="66" y="92">Category 4</text><text x="66" y="126">Category 3</text><text x="66" y="160">Category 2</text><text x="66" y="194">Category 1</text></g>
  <g>
    <rect class="red" x="70" y="80" width="130" height="6"/><rect class="dark" x="70" y="86" width="72" height="6"/><rect class="pink" x="70" y="92" width="116" height="6"/>
    <rect class="red" x="70" y="114" width="78" height="6"/><rect class="dark" x="70" y="120" width="46" height="6"/><rect class="pink" x="70" y="126" width="90" height="6"/>
    <rect class="red" x="70" y="148" width="52" height="6"/><rect class="dark" x="70" y="154" width="114" height="6"/><rect class="pink" x="70" y="160" width="66" height="6"/>
    <rect class="red" x="70" y="182" width="56" height="6"/><rect class="dark" x="70" y="188" width="60" height="6"/><rect class="pink" x="70" y="194" width="112" height="6"/>
  </g>
  <g font-size="4.5" fill="#777"><rect class="red" x="94" y="218" width="3" height="3"/><text x="99" y="221">Series 3</text><rect class="dark" x="124" y="218" width="3" height="3"/><text x="129" y="221">Series 2</text><rect class="pink" x="152" y="218" width="3" height="3"/><text x="157" y="221">Series 1</text></g>
  <g>
    <circle cx="270" cy="86" r="10" class="red"/><circle cx="269" cy="85" r="3" fill="none" stroke="#fff" stroke-width="1.2"/><path d="M271 87 l3 3" stroke="#fff" stroke-width="1.2"/>
    <text class="red lbl" x="290" y="84">Category One</text><text class="lorem" x="290" y="92">Lorem ipsum dolor sit amet, consectetur</text><text class="lorem" x="290" y="98">adipiscing elit, sed do eiusmod</text>
    <circle cx="270" cy="126" r="10" class="dark"/><path d="M266 130 l8 -8" stroke="#fff" stroke-width="2"/>
    <text class="dark lbl" x="290" y="124">Category Two</text><text class="lorem" x="290" y="132">Lorem ipsum dolor sit amet, consectetur</text><text class="lorem" x="290" y="138">adipiscing elit, sed do eiusmod</text>
    <circle cx="270" cy="164" r="10" class="pink"/><path d="M266 168 l4 -8 4 4z" fill="#fff"/>
    <text class="pink lbl" x="290" y="162">Category Three</text><text class="lorem" x="290" y="170">Lorem ipsum dolor sit amet, consectetur</text><text class="lorem" x="290" y="176">adipiscing elit, sed do eiusmod</text>
    <circle cx="270" cy="203" r="10" class="blue"/><circle cx="270" cy="203" r="4" fill="none" stroke="#fff" stroke-width="2" stroke-dasharray="2 1"/>
    <text class="blue lbl" x="290" y="201">Category Four</text><text class="lorem" x="290" y="209">Lorem ipsum dolor sit amet, consectetur</text><text class="lorem" x="290" y="215">adipiscing elit, sed do eiusmod</text>
  </g>
  <rect class="red" x="0" y="254" width="478" height="14"/>
  <text class="copy" x="20" y="263">© Copyright 2017 Lukas Femberg. All rights reserved.</text>
  <rect class="dark" x="430" y="254" width="28" height="14"/><text class="pg" x="444" y="263" text-anchor="middle">45</text>
</svg>

<!-- Row 4 -->
<svg class="slide bullet-chart" style="left:3px;top:693px" viewBox="0 0 478 268">
  <text class="ttl" x="20" y="33">BULLET &amp; CHART AREA</text><rect class="red" x="20" y="40" width="26" height="2"/>
  <text class="logo" x="468" y="27" text-anchor="end">LUKAS FEMBERG</text>
  <g>
    <circle cx="58" cy="82" r="10" class="red"/><circle cx="57" cy="81" r="3" fill="none" stroke="#fff" stroke-width="1.2"/><path d="M59 83 l3 3" stroke="#fff" stroke-width="1.2"/>
    <text class="red lbl" x="79" y="81">Your Text Here</text><text class="lorem" x="79" y="89">Lorem ipsum dolor sit amet, consectetur adipiscing</text><text class="lorem" x="79" y="95">elit, sed do eiusmod</text>
    <circle cx="58" cy="121" r="10" class="dark"/><path d="M54 125 l8 -8" stroke="#fff" stroke-width="2"/>
    <text class="dark lbl" x="79" y="120">Your Text Here</text><text class="lorem" x="79" y="128">Lorem ipsum dolor sit amet, consectetur adipiscing</text><text class="lorem" x="79" y="134">elit, sed do eiusmod</text>
    <circle cx="58" cy="160" r="10" class="pink"/><path d="M54 164 l4 -8 4 4z" fill="#fff"/>
    <text class="pink lbl" x="79" y="159">Your Text Here</text><text class="lorem" x="79" y="167">Lorem ipsum dolor sit amet, consectetur adipiscing</text><text class="lorem" x="79" y="173">elit, sed do eiusmod</text>
    <circle cx="58" cy="199" r="10" class="blue"/><circle cx="58" cy="199" r="4" fill="none" stroke="#fff" stroke-width="2" stroke-dasharray="2 1"/>
    <text class="blue lbl" x="79" y="198">Your Text Here</text><text class="lorem" x="79" y="206">Lorem ipsum dolor sit amet, consectetur adipiscing</text><text class="lorem" x="79" y="212">elit, sed do eiusmod</text>
  </g>
  <line x1="258" y1="191" x2="436" y2="191" stroke="#ccc" stroke-width=".6"/>
  <g>
    <rect class="red" x="264" y="100" width="8" height="91"/><rect class="dark" x="272" y="140" width="8" height="51"/><rect class="pink" x="280" y="149" width="8" height="42"/>
    <rect class="red" x="309" y="138" width="8" height="53"/><rect class="dark" x="317" y="97" width="8" height="94"/><rect class="pink" x="325" y="149" width="8" height="42"/>
    <rect class="red" x="354" y="117" width="8" height="74"/><rect class="dark" x="362" y="153" width="8" height="38"/><rect class="pink" x="370" y="126" width="8" height="65"/>
    <rect class="red" x="399" y="94" width="8" height="97"/><rect class="dark" x="407" y="132" width="8" height="59"/><rect class="pink" x="415" y="84" width="8" height="107"/>
  </g>
  <g font-size="4.5" fill="#777" text-anchor="middle"><text x="276" y="201">Category 1</text><text x="321" y="201">Category 2</text><text x="366" y="201">Category 3</text><text x="411" y="201">Category 4</text></g>
  <g font-size="4.5" fill="#777"><rect class="red" x="307" y="208" width="3" height="3"/><text x="312" y="211">Series 1</text><rect class="dark" x="337" y="208" width="3" height="3"/><text x="342" y="211">Series 2</text><rect class="pink" x="366" y="208" width="3" height="3"/><text x="371" y="211">Series 3</text></g>
  <rect class="red" x="0" y="254" width="478" height="14"/>
  <text class="copy" x="20" y="263">© Copyright 2017 Lukas Femberg. All rights reserved.</text>
  <rect class="dark" x="430" y="254" width="28" height="14"/><text class="pg" x="444" y="263" text-anchor="middle">46</text>
</svg>

<svg class="slide three-steps" style="left:403px;top:693px" viewBox="0 0 478 268">
  <text class="ttl" x="20" y="33">THREE STEPS</text><rect class="red" x="20" y="40" width="26" height="2"/>
  <text class="logo" x="468" y="27" text-anchor="end">LUKAS FEMBERG</text>
  <circle cx="43" cy="90" r="10" class="red"/><g fill="#fff"><rect x="39" y="90" width="2" height="4"/><rect x="42" y="87" width="2" height="7"/><rect x="45" y="89" width="2" height="5"/></g>
  <text class="red lbl" x="65" y="93">Sample Text</text>
  <text x="65" y="107" font-size="5.5" fill="#777">Lorem ipsum dolor sit amet, consectetuer adipiscing elit. Duis</text><text x="65" y="119" font-size="5.5" fill="#777">ligula lorem, consequat eget, tristique nec, auctor quis, purus.</text>
  <circle cx="43" cy="138" r="10" class="dark"/><path d="M39 142 l4 -8 4 4z" fill="#fff"/>
  <text class="dark lbl" x="65" y="141">Sample Text</text>
  <text x="65" y="155" font-size="5.5" fill="#777">Lorem ipsum dolor sit amet, consectetuer adipiscing elit. Duis</text><text x="65" y="167" font-size="5.5" fill="#777">ligula lorem, consequat eget, tristique nec, auctor quis, purus.</text>
  <circle cx="43" cy="186" r="10" class="pink"/><circle cx="42" cy="185" r="3" fill="none" stroke="#fff" stroke-width="1.2"/><path d="M44 187 l3 3" stroke="#fff" stroke-width="1.2"/>
  <text class="pink lbl" x="65" y="189">Sample Text</text>
  <text x="65" y="203" font-size="5.5" fill="#777">Lorem ipsum dolor sit amet, consectetuer adipiscing elit. Duis</text><text x="65" y="215" font-size="5.5" fill="#777">ligula lorem, consequat eget, tristique nec, auctor quis, purus.</text>
  <circle cx="395" cy="86" r="35" fill="none" stroke="#d42030" stroke-width="24"/>
  <path d="M368 117 A36 36 0 1 0 368 161" fill="none" stroke="#231f20" stroke-width="24"/>
  <circle cx="395" cy="188" r="35" fill="none" stroke="#e5177f" stroke-width="24"/>
  <g fill="none" stroke-width="1.2">
    <path d="M383 86h22M386 86v-5h16v5" stroke="#d42030"/><circle cx="394" cy="78" r="3" stroke="#d42030"/>
    <path d="M336 146l6-8 5 4 7-9M334 132v16h22" stroke="#231f20"/>
    <path d="M395 178v6M386 192v-6h18v6M390 196h10" stroke="#e5177f"/><rect x="391" y="174" width="8" height="5" stroke="#e5177f"/>
  </g>
  <rect class="red" x="0" y="254" width="478" height="14"/>
  <text class="copy" x="20" y="263">© Copyright 2017 Lukas Femberg. All rights reserved.</text>
  <rect class="dark" x="430" y="254" width="28" height="14"/><text class="pg" x="444" y="263" text-anchor="middle">47</text>
</svg>

<svg class="slide key-points" style="left:802px;top:693px" viewBox="0 0 478 268">
  <defs><linearGradient id="lakePhoto" x1="0" y1="0" x2="1" y2="1"><stop offset="0" stop-color="#3a3633"/><stop offset=".5" stop-color="#7b7671"/><stop offset="1" stop-color="#262322"/></linearGradient></defs>
  <rect width="478" height="268" fill="url(#lakePhoto)" role="img" aria-label="Photo of dark rippling water with a wooden post"/>
  <rect x="238" y="0" width="240" height="268" fill="#d42030" opacity=".92"/>
  <text x="268" y="56" font-size="15" fill="#fff">KEY POINTS</text>
  <rect class="white" x="268" y="63" width="26" height="2"/>
  <g font-size="7.5" fill="#fff">
    <text x="268" y="98">•   Lorem ipsum dolor sit amet,</text>
    <text x="268" y="119">•   consectetur adipiscing elit, sed do</text>
    <text x="268" y="141">•   eiusmod tempor incididunt ut</text>
    <text x="268" y="162">•   labore et dolore magna aliqua. Ut</text>
    <text x="268" y="184">•   enimad minim veniam, quis nostrud</text>
    <text x="268" y="205">•   exercitation ullamco laboris nisi ut</text>
    <text x="268" y="227">•   aliquip ex ea commodo consequat</text>
  </g>
</svg>

<!-- Row 5 -->
<svg class="slide three-bullets" style="left:3px;top:922px" viewBox="0 0 478 268">
  <defs><linearGradient id="portraitPhoto" x1="0" y1="0" x2="1" y2="0"><stop offset="0" stop-color="#d8d8d6"/><stop offset=".6" stop-color="#cfcdca"/><stop offset="1" stop-color="#9c9a97"/></linearGradient></defs>
  <text class="ttl" x="20" y="33">THREE BULLETS AREA</text><rect class="red" x="20" y="40" width="26" height="2"/>
  <text class="logo" x="468" y="27" text-anchor="end">LUKAS FEMBERG</text>
  <rect x="0" y="52" width="478" height="113" fill="url(#portraitPhoto)" role="img" aria-label="Portrait photo of the coach against a light wall"/>
  <circle cx="89" cy="175" r="28" class="red"/>
  <g stroke="#fff" stroke-width="2" fill="none"><circle cx="80" cy="175" r="4"/><circle cx="97" cy="166" r="4"/><circle cx="97" cy="184" r="4"/><path d="M84 173l9-5M84 177l9 5"/></g>
  <circle cx="241" cy="174" r="28" class="dark"/>
  <g stroke="#fff" stroke-width="1.8" fill="none"><path d="M229 170l12-6 12 6-12 6z"/><path d="M229 176l12 6 12-6"/><path d="M229 181l12 6 12-6"/></g>
  <circle cx="395" cy="175" r="28" class="pink"/>
  <path d="M388 189h16v-3h-3c0-6 4-8 2-15-2-5-8-7-12-5l-4 7 3 2 4-2c-1 4-4 7-6 13z" fill="#fff"/>
  <g class="lorem" text-anchor="middle">
    <text x="89" y="214">Lorem ipsum dolor sit amet,</text><text x="89" y="221">consectetur adipiscing elit, sed do</text><text x="89" y="228">eiusmod tempor incididunt ut</text><text x="89" y="235">labore</text>
    <text x="241" y="214">Lorem ipsum dolor sit amet,</text><text x="241" y="221">consectetur adipiscing elit, sed do</text><text x="241" y="228">eiusmod tempor incididunt ut</text><text x="241" y="235">labore</text>
    <text x="395" y="214">Lorem ipsum dolor sit amet,</text><text x="395" y="221">consectetur adipiscing elit, sed do</text><text x="395" y="228">eiusmod tempor incididunt ut</text><text x="395" y="235">labore</text>
  </g>
  <rect class="red" x="0" y="254" width="478" height="14"/>
  <text class="copy" x="20" y="263">© Copyright 2017 Lukas Femberg. All rights reserved.</text>
  <rect class="dark" x="430" y="254" width="28" height="14"/><text class="pg" x="444" y="263" text-anchor="middle">49</text>
</svg>

<svg class="slide social-media" style="left:403px;top:922px" viewBox="0 0 478 268">
  <text class="ttl" x="20" y="33">SOCIAL MEDIA MARKETING</text><rect class="red" x="20" y="40" width="26" height="2"/>
  <text class="logo" x="468" y="27" text-anchor="end">LUKAS FEMBERG</text>
  <g fill="#dcdcdc"><rect x="108" y="102" width="30" height="152"/><rect x="186" y="102" width="30" height="152"/><rect x="263" y="102" width="30" height="152"/><rect x="340" y="102" width="30" height="152"/></g>
  <rect class="red" x="108" y="120" width="30" height="134"/>
  <rect class="dark" x="186" y="172" width="30" height="82"/>
  <rect class="pink" x="263" y="138" width="30" height="116"/>
  <rect class="blue" x="340" y="198" width="30" height="56"/>
  <g fill="#fff" font-size="13" text-anchor="middle"><text x="123" y="138">88</text><text x="201" y="190">54</text><text x="278" y="156">76</text><text x="355" y="216">37</text></g>
  <circle cx="123" cy="75" r="23" class="red"/><circle cx="201" cy="75" r="23" class="dark"/><circle cx="278" cy="75" r="23" class="pink"/><circle cx="355" cy="75" r="23" class="blue"/>
  <g fill="#fff" font-size="8" font-weight="700" text-anchor="middle"><text x="123" y="78">Alpha</text><text x="201" y="78">Beta</text><text x="278" y="78">Gamma</text><text x="355" y="78">Delta</text></g>
  <rect class="red" x="0" y="254" width="478" height="14"/>
  <text class="copy" x="20" y="263">© Copyright 2017 Lukas Femberg. All rights reserved.</text>
  <rect class="dark" x="430" y="254" width="28" height="14"/><text class="pg" x="444" y="263" text-anchor="middle">50</text>
</svg>

<svg class="slide thank-you" style="left:802px;top:922px" viewBox="0 0 478 268">
  <defs><linearGradient id="coachPhoto" x1="0" y1="0" x2="1" y2="0"><stop offset="0" stop-color="#3c3c3c"/><stop offset=".6" stop-color="#5a5a5a"/><stop offset="1" stop-color="#3a3a3a"/></linearGradient></defs>
  <rect width="478" height="268" fill="url(#coachPhoto)" role="img" aria-label="Dark-toned portrait photo of the coach"/>
  <text x="28" y="82" font-size="28" font-weight="700" fill="#fff">THANK YOU</text>
  <text x="32" y="103" font-size="11" fill="#fff">SEND YOUR FEEDBACK</text>
  <g fill="#fff">
    <path d="M27 170l5-5 5 5h-2v4h-6v-4z"/>
    <path d="M28 184c1 4 3 6 7 7l1-2-2-2-1 1c-1 0-2-1-3-3l1-1-2-2z"/>
    <rect x="27" y="201" width="9" height="6"/>
    <circle cx="31.5" cy="219" r="4.5"/>
  </g>
  <path d="M27 201l4.5 3 4.5-3" stroke="#444" stroke-width=".8" fill="none"/>
  <g font-size="5.5" fill="#fff"><text x="43" y="168">Lindenweg 12</text><text x="43" y="174">37083 Musterstadt</text><text x="43" y="189">0151 20398475</text><text x="43" y="206">info@lukas-femberg.de</text><text x="43" y="221">www.lukas-femberg.de</text></g>
  <path d="M478 150 L478 268 L310 268Z" fill="#fff"/>
  <path d="M478 148 L306 268" stroke="#d42030" stroke-width="2"/>
  <text class="logo" x="470" y="246" text-anchor="end">LUKAS FEMBERG</text>
</svg>

</body>
</html>
```